poster design for mountainbike & trail run race

I am looking for a poster design for a charitable mountain bike and trail run race. It should be something fun, colorful, epic, which can attract participants. The area in which the competition takes place is dominated by hills and by the Nera river which has a beautiful gorge. I am attaching our last year poster, which we like, but would like this year to be a bit more epic, exciting for the possible participants. The poster should have a place where I can add the sponsor logos (approx 20 logos), which I will do by myself, in the following months (will need editable design format). We will also need the poster in both 16x9 and 4x3 formats.
Text:
Headline: "Culmea Fagetan Mountain Bike and Trail Run Race"
small headline: "Editia a-7a"
small headline: "Sasca Romana, 8-9 IUNIE 2024"
other text:
"8 IUNIE - Concurs Mountain Bike & Concert
9 IUNIE - Concurs Trail Run"
text for enrollments: "inscrieri pe www.vultoridetur.ro"

Thank you!

Target Market(s)

people aged 18-50, doing sports, participating to competitions

Requirements
Must have
• clean, proefesional design. The poster will be presented in social media as well on bilboards

```html
<!DOCTYPE html>
<html lang="ro">
<head>
<meta charset="utf-8">
<title>Culmea Fagetan Mountain Bike and Trail Run Race</title>
<link href="https://fonts.googleapis.com/css2?family=Bebas+Neue&family=Lobster&family=Poppins:wght@500;600&family=Rye&display=swap" rel="stylesheet">
<style>
  :root {
    --page: #ffffff;
    --poster-bg: #2b2628;
    --poster-deep: #221c20;
    --orange: #d9782c;
    --orange-dark: #a6521c;
    --amber: #f0a64a;
    --cream: #f6e6c4;
    --white: #f4efe8;
    --wood: #8a5530;
    --wood-light: #b77c4a;
    --rust: #b77a5a;
    --cord: #c9a27a;
  }
  * { margin: 0; padding: 0; box-sizing: border-box; }
  html, body { width: 1200px; height: 2956px; overflow: hidden; background: var(--page); }

  .poster {
    position: absolute; left: 50px; top: 500px;
    width: 1100px; height: 1956px;
    background: var(--poster-bg);
    overflow: hidden;
    box-shadow: 0 10px 30px rgba(0,0,0,.35);
    text-align: center;
  }
  .poster > * { position: absolute; left: 0; width: 100%; }

  .scene-art {
    top: 440px; height: 880px;
    border-radius: 550px 550px 0 0;
    background:
      radial-gradient(circle at 50% 30%, var(--cream) 0 14%, rgba(246,230,196,0) 28%),
      radial-gradient(ellipse 80% 45% at 50% 42%, #e09a55 0%, rgba(224,154,85,0) 70%),
      linear-gradient(180deg, #b85f26 0%, #cf7a36 30%, #c26a2c 48%, #7a4222 64%, #3a2822 80%, var(--poster-deep) 92%, var(--poster-bg) 100%);
  }

  .title {
    top: 40px;
    font-family: "Lobster", cursive;
    font-size: 160px; line-height: 1;
    background: linear-gradient(180deg, var(--amber) 10%, var(--orange) 55%, var(--orange-dark) 100%);
    -webkit-background-clip: text; background-clip: text; color: transparent;
  }
  .subtitle {
    top: 222px;
    font-family: "Bebas Neue", sans-serif;
    font-size: 78px; line-height: 1; color: var(--white);
  }
  .location {
    top: 310px;
    font-family: "Rye", serif;
    font-size: 62px; line-height: 1; letter-spacing: 3px; color: var(--rust);
  }

  .edition-sign { top: 370px; height: 150px; }
  .edition-sign .cord { position: absolute; inset: 0; width: 100%; height: 100%; }
  .edition-sign .board {
    position: absolute; left: 400px; top: 42px; width: 298px; height: 100px;
    background: linear-gradient(180deg, var(--wood-light), var(--wood) 60%, #6b3d22);
    border-radius: 4px;
    box-shadow: 0 4px 8px rgba(0,0,0,.45);
    font-family: "Poppins", sans-serif; font-weight: 600;
    font-size: 40px; line-height: 100px; color: var(--cream);
  }

  .date {
    top: 1296px;
    font-family: "Bebas Neue", sans-serif;
    font-size: 138px; line-height: 1; letter-spacing: 2px;
    background: linear-gradient(180deg, var(--amber), var(--orange));
    -webkit-background-clip: text; background-clip: text; color: transparent;
  }
  .schedule {
    top: 1430px;
    font-family: "Bebas Neue", sans-serif;
    font-size: 70px; line-height: 71px; color: var(--white);
    list-style: none;
  }
  .schedule .day { color: var(--orange); margin-right: 18px; }

  .signup {
    top: 1578px; left: 170px; width: 760px; height: 62px;
    background: var(--cream);
    border: 4px solid var(--amber);
    border-radius: 31px;
    font-family: "Poppins", sans-serif; font-weight: 600;
    font-size: 40px; line-height: 54px; color: #2a1e18;
  }

  .socials {
    top: 1674px;
    display: flex; justify-content: center; gap: 34px;
    font-family: "Poppins", sans-serif; font-weight: 500;
    font-size: 28px; line-height: 40px; color: var(--orange);
  }
  .socials .handle { display: flex; align-items: center; gap: 12px; }
  .socials .mark { width: 24px; height: 24px; background: var(--white); border-radius: 4px; }
  .socials .mark.round { border-radius: 50%; }

  .sponsors {
    top: 1732px;
    font-family: "Poppins", sans-serif; font-weight: 500;
    font-size: 15px; letter-spacing: 9px; color: var(--white);
  }
</style>
</head>
<body>
  <main class="poster">
    <div class="scene-art" role="img" aria-label="Illustration: mountain biker and trail runner silhouettes on a hillside path, orange mountains and pine forest under a large sunset disc"></div>

    <h1 class="title">Culmea Fagetan</h1>
    <p class="subtitle">Mountain Bike and Trail Run Race</p>
    <p class="location">SASCA ROMANA</p>

    <div class="edition-sign">
      <svg class="cord" viewBox="0 0 1100 150" aria-hidden="true">
        <path d="M470 44 L550 14 L630 44" stroke="var(--cord)" stroke-width="4" fill="none"/>
        <circle cx="550" cy="14" r="5" fill="var(--cord)"/>
      </svg>
      <div class="board">Editia a-7a</div>
    </div>

    <p class="date">8-9 IUNIE 2024</p>
    <ul class="schedule">
      <li><span class="day">8 IUNIE</span>Concurs Mountain Bike &amp; Concert</li>
      <li><span class="day">9 IUNIE</span>Concurs Trail Run</li>
    </ul>

    <p class="signup">inscrieri pe www.vultoridetur.ro</p>

    <div class="socials">
      <span class="handle"><span class="mark"></span>CulmeaFagetanMTB</span>
      <span class="handle"><span class="mark round"></span>culmeafagetan.bike.run</span>
    </div>

    <p class="sponsors">SPONSORED BY</p>
  </main>
</body>
</html>
```